Advertisement Design Project

We need to design a backdrop and 2 roll up banners and table skirts for tradeshow displays...We have a current logo design and a basic idea how we need the artwork too look....need a designer to put it all together!!

Target Market(s)

Our target is mostly women...Its for the canadian and american market!!

Requirements
Must have
• What VORANTE means is "free" to be free....freedom!!!!
Need to have a good vision of what a final display for trade shows should look like!!
attractive colours..not too bold....clean but fun look!!!!
-express your individuality
-interchangeable
-create your own style
-Designed by you
-endless possibilities
Nice to have
• -freedom to express your own style
-butterflies
-Birds
-colourful
websites that have similar product line
www.tazipendesigns.example
www.brolvadesigns.example
www.quelpi-rotterbay.example

Should not have
• No Direct infringement to the sites listed above!!!

```html
<!DOCTYPE html>
<html lang="en">
<head>
<meta charset="utf-8">
<title>VORANTE – Express Your Individuality Backdrop</title>
<link rel="stylesheet" href="https://fonts.googleapis.com/css2?family=Oswald:wght@500;600&display=swap">
<style>
  :root {
    --paper-light: #f7f6f4;
    --paper-mid: #ecebe8;
    --ink: #1f1f1f;
    --orchid: #b551a9;
    --plum: #8e2f72;
    --rose: #e7c3c9;
    --blush: #f3dcd8;
    --accent-soft-green: rgba(63, 163, 95, 0.22);
    --accent-soft-berry: rgba(217, 67, 79, 0.20);
    --accent-soft-lemon: rgba(231, 220, 58, 0.22);
  }
  * { margin: 0; padding: 0; box-sizing: border-box; }
  html, body {
    width: 1200px;
    height: 849px;
    overflow: hidden;
  }
  body {
    font-family: "Oswald", "Arial Narrow", sans-serif;
    background: var(--paper-mid);
  }
  .backdrop {
    position: relative;
    width: 1200px;
    height: 849px;
    overflow: hidden;
    background: linear-gradient(90deg, var(--paper-mid) 0%, var(--paper-light) 45%, var(--paper-light) 70%, var(--paper-mid) 100%);
  }
  .brand-name {
    position: absolute;
    top: 112px;
    left: 0;
    width: 1200px;
    text-align: center;
    font-weight: 500;
    font-size: 64px;
    line-height: 1;
    letter-spacing: 10px;
    color: var(--ink);
  }
  .headline {
    position: absolute;
    left: 78px;
    top: 284px;
    text-transform: uppercase;
    color: var(--ink);
    font-weight: 600;
    line-height: 1;
  }
  .headline-main {
    display: block;
    font-size: 72px;
    letter-spacing: 0.5px;
  }
  .headline-sub {
    display: block;
    margin-top: 6px;
    font-size: 41px;
    letter-spacing: 0.3px;
  }
  .headline-accent { color: var(--orchid); }
  .butterfly-art {
    position: absolute;
    left: 836px;
    top: 266px;
    width: 250px;
    height: 160px;
    border-radius: 28px;
    background: linear-gradient(135deg, var(--accent-soft-green) 0%, var(--accent-soft-berry) 50%, var(--accent-soft-lemon) 100%);
  }
  .floral-art {
    position: absolute;
    left: 0;
    bottom: 0;
    width: 1160px;
    height: 470px;
    background:
      radial-gradient(ellipse at 42% 78%, rgba(142, 47, 114, 0.75) 0%, rgba(181, 81, 169, 0.45) 30%, transparent 60%),
      radial-gradient(ellipse at 60% 40%, rgba(231, 195, 201, 0.8) 0%, transparent 55%),
      radial-gradient(ellipse at 20% 85%, rgba(243, 220, 216, 0.9) 0%, transparent 60%);
  }
</style>
</head>
<body>
  <main class="backdrop">
    <div class="floral-art" role="img" aria-label="Soft pink and purple floral illustration with swirling lines and circles"></div>
    <div class="butterfly-art" role="img" aria-label="Colourful butterfly illustration in green, red, aqua and yellow"></div>
    <div class="brand-name">VORANTE</div>
    <h1 class="headline">
      <span class="headline-main">Express</span>
      <span class="headline-sub">Your <span class="headline-accent">Individuality</span></span>
    </h1>
  </main>
</body>
</html>
```